CD-Cover Desig für neues Album eines Liedermacher-Duos
Zielgruppe
Wir sind ein Liedermacher-Duo und benötigen für unser neues Album mit dem Titel 'Kiesel' ein Cover.
Infos über den Themenbereich der Songs findet man hier: https://www.vorhabenwerk.de/cd-kiesel
Aufgabenstellung
Cover könnte schlicht sein... oder auch kreativ verspielt mit warmen Farben und Formen... aber nicht kitschig.
'Kiesel' im Sinne von Geborgenheit also kein verzehrendes Feuer.. eher sonnig.
Evtl. könnte man unsere beiden Hauptinstrumente (Geige und Gitarre) andeuten.
Sonst stehen auf dem Cover nur noch unsere Namen: Dorothea Lindner & Jörg Haberl

```html
<!DOCTYPE html>
<html lang="de">
<head>
<meta charset="utf-8">
<title>Kiesel – Dorothea Lindner &amp; Jörg Haberl</title>
<link rel="stylesheet" href="https://fonts.googleapis.com/css2?family=Inter+Tight:wght@200;300&display=swap">
<style>
  :root {
    --page: #ffffff;
    --cover-edge: #e6d6c4;
    --title: #9c1c5c;
    --names: #2b2b2b;
    --tone-light: #fff4c4;
    --tone-yellow: #fdd65a;
    --tone-orange: #f5a05a;
    --tone-coral: #ef8566;
  }
  html, body {
    margin: 0;
    padding: 0;
    width: 1200px;
    height: 1200px;
    overflow: hidden;
    background: var(--page);
  }
  .album-cover {
    position: absolute;
    left: 228px;
    top: 243px;
    width: 711px;
    height: 714px;
    border: 1px solid var(--cover-edge);
    box-sizing: border-box;
    overflow: hidden;
    background: var(--page);
  }
  .cover-artwork {
    position: absolute;
    inset: 6px;
    background: linear-gradient(
      180deg,
      var(--page) 0%,
      var(--tone-light) 10%,
      var(--tone-yellow) 28%,
      var(--tone-orange) 40%,
      var(--tone-coral) 50%,
      var(--tone-orange) 62%,
      var(--tone-yellow) 76%,
      var(--tone-light) 88%,
      var(--page) 100%
    );
  }
  .album-title {
    position: absolute;
    left: 50px;
    top: 100px;
    margin: 0;
    font-family: "Inter Tight", sans-serif;
    font-weight: 200;
    font-size: 120px;
    line-height: 1;
    letter-spacing: 0.4em;
    color: var(--title);
    white-space: nowrap;
  }
  .artist-names {
    position: absolute;
    left: 0;
    right: 0;
    top: 604px;
    margin: 0;
    text-align: center;
    font-family: "Inter Tight", sans-serif;
    font-weight: 300;
    font-size: 19px;
    line-height: 1.2;
    letter-spacing: 0.3em;
    color: var(--names);
    white-space: nowrap;
  }
</style>
</head>
<body>
  <main class="album-cover">
    <div class="cover-artwork" role="img" aria-label="Photograph of a warm sunset over calm rippling water in yellow, orange and soft red tones"></div>
    <h1 class="album-title">KIESEL</h1>
    <p class="artist-names">DOROTHEA LINDNER &amp; JÖRG HABERL</p>
  </main>
</body>
</html>
```